Tool kit box label .

Looking for a label design to attach to our engine tool kit, will have logo design included for brand KRONVALE TOOLS . Label also to have this text : Fuel Injection pump kit .
The sticker will be put on the packages shown in attachments.
Target Market(s)
Automotive workshops
Colors
fece3e
1b1b1b
Requirements
Must have
- Cool industrial look

```html
<!DOCTYPE html>
<html lang="en">
<head>
<meta charset="utf-8">
<title>Kronvale Tools – Fuel Injection Pump Kit Label</title>
<link rel="stylesheet" href="https://fonts.googleapis.com/css2?family=Anton&display=swap">
<style>
  :root {
    --brand-yellow: #fece3e;
    --brand-yellow-deep: #f5bf1f;
    --brand-black: #1b1b1b;
    --panel-dark: #0e0e0f;
    --panel-mid: #1f2022;
    --frame-light: #ececec;
    --frame-dark: #7d7d7d;
    --ink: #111111;
  }
  html, body {
    margin: 0;
    padding: 0;
    width: 1200px;
    height: 730px;
    overflow: hidden;
    background: #ffffff;
  }
  .label {
    position: relative;
    width: 1200px;
    height: 730px;
    overflow: hidden;
    background: var(--brand-yellow);
  }
  .label-shapes {
    position: absolute;
    inset: 0;
  }
  .brand-name {
    position: absolute;
    left: 106px;
    top: 96px;
    width: 400px;
    margin: 0;
    text-align: center;
    font-family: "Anton", "Impact", sans-serif;
    font-weight: 400;
    font-size: 34px;
    line-height: 33px;
    letter-spacing: 1px;
    color: var(--ink);
  }
  .product-title {
    position: absolute;
    left: 32px;
    top: 226px;
    width: 500px;
    margin: 0;
    text-align: center;
    font-family: "Anton", "Impact", sans-serif;
    font-weight: 400;
    font-size: 104px;
    line-height: 117px;
    letter-spacing: 4px;
    color: var(--ink);
  }
  .product-title span {
    display: block;
  }
  .engine-visual {
    position: absolute;
    left: 672px;
    top: 120px;
    width: 414px;
    height: 456px;
    border-radius: 50%;
    background: radial-gradient(ellipse at 50% 48%, #55575b 0%, #323437 45%, #1c1d1f 75%, rgba(20,20,22,0) 100%);
  }
</style>
</head>
<body>
<main class="label">
  <svg class="label-shapes" width="1200" height="730" viewBox="0 0 1200 730" aria-hidden="true">
    <defs>
      <linearGradient id="yellowField" x1="0" y1="0" x2="1" y2="1">
        <stop offset="0" stop-color="var(--brand-yellow)"/>
        <stop offset="1" stop-color="var(--brand-yellow-deep)"/>
      </linearGradient>
      <linearGradient id="darkField" x1="0" y1="0" x2="1" y2="1">
        <stop offset="0" stop-color="var(--panel-mid)"/>
        <stop offset="1" stop-color="var(--panel-dark)"/>
      </linearGradient>
      <linearGradient id="steelFrame" x1="0" y1="0" x2="1" y2="0">
        <stop offset="0" stop-color="var(--frame-dark)"/>
        <stop offset="0.45" stop-color="var(--frame-dark)"/>
        <stop offset="0.7" stop-color="var(--frame-light)"/>
        <stop offset="1" stop-color="var(--frame-light)"/>
      </linearGradient>
    </defs>

    <rect class="field-yellow" width="1200" height="730" fill="url(#yellowField)"/>

    <polygon class="chevron-band" points="738,0 790,0 578,360 800,730 750,730 528,360" fill="var(--brand-black)"/>

    <polygon class="field-dark" points="790,0 1200,0 1200,730 800,730 578,360" fill="url(#darkField)"/>
    <polyline class="chevron-edge" points="790,0 578,360 800,730" fill="none" stroke="#3a3b3d" stroke-width="1.5"/>

    <rect class="steel-frame" x="48" y="48" width="1104" height="630" rx="30" fill="none" stroke="url(#steelFrame)" stroke-width="6"/>

    <g class="reg-marks" fill="none" stroke="var(--brand-black)" stroke-width="1.5">
      <g transform="translate(600,14)"><circle r="7" fill="#ffffff"/><path d="M-11 0H11M0 -11V11"/></g>
      <g transform="translate(600,716)"><circle r="7" fill="#ffffff"/><path d="M-11 0H11M0 -11V11"/></g>
      <g transform="translate(14,360)"><circle r="7" fill="#ffffff"/><path d="M-11 0H11M0 -11V11"/></g>
      <g transform="translate(1184,360)" stroke="#bdbdbd"><circle r="7" fill="#ffffff"/><path d="M-11 0H11M0 -11V11"/></g>
      <g transform="translate(14,50)"><circle r="5" fill="#ffffff"/></g>
      <g transform="translate(14,680)"><circle r="5" fill="#ffffff"/></g>
      <g transform="translate(1186,50)" stroke="#bdbdbd"><circle r="5" fill="#ffffff"/></g>
      <g transform="translate(1186,680)" stroke="#bdbdbd"><circle r="5" fill="#ffffff"/></g>
    </g>
  </svg>

  <p class="brand-name">KRONVALE<br>TOOLS</p>

  <h1 class="product-title">
    <span>FUEL</span>
    <span>INJECTION</span>
    <span>PUMP KIT</span>
  </h1>

  <div class="engine-visual" role="img" aria-label="Product photo of a compact diesel engine with alternator, belts and fuel filter"></div>
</main>
</body>
</html>
```